3 Banner Designs

We are looking for someone to create 3 designs with the dimensions of 310mm wide x 432mm high with a 300dpi. This would just be a picture design only, NO FLASH req'd.

Each design would need to promote a different part:

- Like our Gatherly page; special offers (gatherly.example/CheapRunwayCarStayPerth)
- Leave a review on Rateloop (rateloop.example/biz/cheap-runway-car-stay-berry-hill)
- Our travel blog (blog.cheaprunwaycarstay.example)
Updates

The dimensions have changed to 310mm x 432mm.

Target Market(s)

Our target market is varied; the one thing that they have in common is that they travel.

Industry/Entity Type

Travel

Font styles to use
Sans Serif
Script

Colors

Designer to choose colors to be used in the design.

Requirements
Must have
• For the Gatherly banner, I would like it to be very simple with a solid blue background with the 'Gatherly Nod Icon' image with the text 'Special Offers, Travel Tips & Reviews' 'Like Our Gatherly page'.

For the Rateloop Ad, I would like it to be a solid red with the Rateloop! logo. Include the text 'Let us know what you thought of our service'.

I'd like something a little different about the third banner that directs users to our travel blog. Include the text 'For Tips and Tricks for your next holiday, check out our new Travel Blog'.

```html
<!DOCTYPE html>
<html lang="en">
<head>
<meta charset="utf-8">
<title>Travel Blog Banner</title>
<link rel="stylesheet" href="https://fonts.googleapis.com/css2?family=Oswald:wght@300;400&display=swap">
<style>
  :root {
    --violet: #7a3f9e;
    --plum: #8c3a78;
    --rose: #c0486a;
    --coral: #d85a6a;
    --teal: #49b8c4;
    --lilac: #a98cd0;
    --panel-dark: rgba(50, 30, 70, 0.72);
    --panel-wine: rgba(96, 24, 48, 0.78);
    --map-light: #f2e6ec;
    --map-mid: #e4cfdc;
    --ink-light: #ffffff;
  }
  * { margin: 0; padding: 0; box-sizing: border-box; }
  html, body { width: 863px; height: 1200px; overflow: hidden; }
  body { font-family: 'Oswald', 'Arial Narrow', sans-serif; color: var(--ink-light); }

  .banner {
    position: relative;
    width: 863px;
    height: 1200px;
    overflow: hidden;
    background:
      radial-gradient(ellipse 420px 520px at 840px 140px, var(--teal) 0%, rgba(73,184,196,0) 100%),
      radial-gradient(ellipse 500px 600px at 430px 560px, var(--coral) 0%, rgba(216,90,106,0) 100%),
      radial-gradient(ellipse 420px 600px at 60px 500px, var(--violet) 0%, rgba(122,63,158,0) 100%),
      radial-gradient(ellipse 420px 400px at 820px 1100px, var(--lilac) 0%, rgba(169,140,208,0) 100%),
      radial-gradient(ellipse 400px 420px at 120px 1080px, var(--teal) 0%, rgba(73,184,196,0) 100%),
      linear-gradient(160deg, var(--plum) 0%, var(--rose) 50%, var(--violet) 100%);
  }

  .headline-box {
    position: absolute;
    left: 178px; top: 0;
    width: 512px; height: 138px;
    background: var(--panel-dark);
    text-align: center;
    padding-top: 20px;
    font-weight: 400;
  }
  .headline-box .line-main { font-size: 40px; line-height: 48px; letter-spacing: 0.5px; }
  .headline-box .line-sub  { font-size: 28px; line-height: 40px; font-weight: 300; letter-spacing: 0.5px; }

  .blog-panel {
    position: absolute;
    left: 78px; top: 184px;
    width: 719px; height: 645px;
    background: var(--panel-wine);
  }
  .world-map {
    position: absolute;
    left: 52px; top: 32px;
    width: 632px; height: 359px;
    border-radius: 6px;
    background: radial-gradient(ellipse at 40% 45%, var(--map-light) 0%, var(--map-mid) 60%, rgba(228,207,220,0.35) 100%);
  }
  .blog-call {
    position: absolute;
    left: 0; right: 0; top: 505px;
    text-align: center;
    font-weight: 400;
  }
  .blog-call .line-a { font-size: 48px; line-height: 56px; }
  .blog-call .line-b { font-size: 48px; line-height: 56px; }

  .icon-box {
    position: absolute;
    left: 247px; top: 880px;
    width: 374px; height: 320px;
    background: var(--panel-dark);
  }
  .icon-box svg { position: absolute; left: 75px; top: 50px; }
</style>
</head>
<body>
  <main class="banner">
    <header class="headline-box">
      <p class="line-main">FOR TIPS AND TRICKS</p>
      <p class="line-sub">FOR YOUR NEXT HOLIDAY</p>
    </header>

    <section class="blog-panel">
      <div class="world-map" role="img" aria-label="White world map showing the continents"></div>
      <h1 class="blog-call">
        <span class="line-a">CHECK OUT OUR</span><br>
        <span class="line-b">NEW TRAVEL BLOG</span>
      </h1>
    </section>

    <aside class="icon-box">
      <svg width="224" height="224" viewBox="0 0 224 224" aria-label="Airplane icon" role="img">
        <circle cx="112" cy="112" r="104" fill="none" stroke="#ffffff" stroke-width="8"/>
        <g fill="#ffffff" transform="rotate(-12 112 112)">
          <path d="M30 112 C30 104 40 101 52 101 L178 101 C194 101 204 106 204 112 C204 118 194 123 178 123 L52 123 C40 123 30 120 30 112 Z"/>
          <path d="M108 101 L150 52 L166 52 L140 101 Z"/>
          <path d="M108 123 L150 172 L166 172 L140 123 Z"/>
          <path d="M44 101 L36 78 L48 78 L64 101 Z"/>
          <path d="M44 123 L36 140 L48 140 L64 123 Z"/>
        </g>
      </svg>
    </aside>
  </main>
</body>
</html>
```